Corliss Chemical Products Label for 5L & 20L cleaning chemical products

I need a new label that is a modernised version of what is attached. The new label needs to be 275mm across 165mm high. The label needs to have a "quite zone" (all white band) ACROSS THE VERY TOP of at least 75mm. This is very important. I don't mind if there is colour that fades to all white at the top or if the label is predominantly all white. I am happy to have the "pond drop" removed.
Also; we thermal print over the base label, so most of the attached labels are ones that have had the thermal print already. The other is one that I have made notes on. You will see that I have five colours. This is so that we can colour code our products. Please ensure that your design has a dominant colour as we will need to have five or six colour variations.
Please make sure that I have room on the label for information.
Thank you Tobias

update 14/12/2015. Hi to all working on my project. With the designs you submit please ensure that there is:
1. 75mm band at the top that is plain white
2. on each side of the label a band that is 60mm that is all white
This is so we can incorporate safety and instructional information when we thermal print over the top.
Thankyou Tobias

Reason: I have increased the deadline to encourage more designs to come through and to give designers the best chance at providing quality designs.

Target Market(s)

Industrial / Commercial Cleaning Chemical Market

Requirements
Must have
• white band across the top that is 75mm wide
Should not have
• Any text except for the Corliss Chemical Products. We will thermally print the address and contact numbers

```html
<!DOCTYPE html>
<html lang="en">
<head>
<meta charset="utf-8">
<title>Corliss Chemical Products Label</title>
<link href="https://fonts.googleapis.com/css2?family=Open+Sans:wght@700;800&display=swap" rel="stylesheet">
<style>
  :root {
    --paper: #ffffff;
    --navy: #1a1377;
    --orange: #f9a51a;
    --mist: #e6e6e6;
    --frame: #1a1377;
  }
  html, body {
    margin: 0;
    padding: 0;
    width: 1200px;
    height: 773px;
    overflow: hidden;
    background: var(--paper);
  }
  .label {
    position: relative;
    width: 1200px;
    height: 773px;
    background: var(--paper);
  }
  .info-band {
    position: absolute;
    top: 79px;
    width: 195px;
    height: 612px;
    border: 3px solid var(--frame);
    box-sizing: border-box;
    background: var(--paper);
  }
  .info-band--left { left: 88px; }
  .info-band--right { left: 926px; }
  .front-panel {
    position: absolute;
    left: 294px;
    top: 79px;
    width: 617px;
    height: 615px;
  }
  .front-panel svg {
    display: block;
    width: 100%;
    height: 100%;
  }
  .brand-name {
    font-family: "Open Sans", sans-serif;
    font-weight: 800;
    font-size: 40px;
    fill: var(--navy);
  }
  .brand-line {
    font-family: "Open Sans", sans-serif;
    font-weight: 800;
    font-size: 20px;
    fill: var(--navy);
  }
</style>
</head>
<body>
  <div class="label">
    <div class="info-band info-band--left"></div>

    <div class="front-panel">
      <svg viewBox="0 0 329 328" xmlns="http://www.w3.org/2000/svg">
        <defs>
          <linearGradient id="quiet-fade" x1="0" y1="0" x2="0" y2="1">
            <stop offset="0" stop-color="#ffffff" stop-opacity="1"/>
            <stop offset="1" stop-color="#ffffff" stop-opacity="0"/>
          </linearGradient>
        </defs>
        <rect class="backdrop" width="329" height="328" fill="var(--orange)"/>
        <path class="swoosh" fill="var(--mist)"
              d="M0,150 C60,62 190,22 329,14 L329,188 C300,262 170,308 0,318 Z"/>
        <path class="swoosh-edge-top" fill="var(--navy)"
              d="M0,136 C60,48 190,8 329,2 L329,12 C190,20 60,62 0,158 Z"/>
        <path class="swoosh-edge-bottom" fill="var(--navy)"
              d="M0,316 C170,306 300,260 329,186 L329,232 C300,290 170,318 0,324 Z"/>
        <rect class="quiet-zone" x="0" y="0" width="329" height="150" fill="var(--paper)"/>
        <rect class="quiet-zone-fade" x="0" y="150" width="329" height="22" fill="url(#quiet-fade)"/>
        <text class="brand-name" x="164" y="222" text-anchor="middle">Corliss</text>
        <text class="brand-line" x="164" y="248" text-anchor="middle">Chemical Products</text>
      </svg>
    </div>

    <div class="info-band info-band--right"></div>
  </div>
</body>
</html>
```